Business card for medical clinic

I need an upmarket, modern medical/health business card for my clinic

Contact Information for Business Card

name, address, email, qr code

```html
<!DOCTYPE html>
<html lang="en">
<head>
<meta charset="utf-8">
<title>Meridian Care Clinic – Business Card</title>
<link rel="stylesheet" href="https://fonts.googleapis.com/css2?family=Montserrat:wght@400;500;600&family=Saira:wght@600&display=swap">
<style>
  :root {
    --backdrop: #9b9b9b;
    --card: #ffffff;
    --brand-blue: #0a8fc6;
    --brand-navy: #1b5e86;
    --ink: #1f2230;
    --soft-top: #d6d9de;
    --soft-bottom: #cdeefb;
  }
  * { margin: 0; padding: 0; box-sizing: border-box; }
  html, body { width: 1200px; height: 1182px; overflow: hidden; }
  body {
    background: var(--backdrop);
    position: relative;
    font-family: "Montserrat", sans-serif;
    color: var(--ink);
  }
  .card {
    position: absolute;
    left: 270px;
    width: 660px;
    height: 386px;
    background: var(--card);
    overflow: hidden;
  }
  .card-front { top: 122px; }
  .card-back { top: 668px; }

  .brand {
    position: absolute;
    display: flex;
    align-items: center;
  }
  .brand-dot {
    border-radius: 50%;
    background: var(--brand-blue);
    flex: none;
  }
  .brand-name {
    font-family: "Montserrat", sans-serif;
    font-weight: 500;
    color: var(--brand-navy);
    letter-spacing: 0.06em;
    line-height: 1.15;
  }
  .card-front .brand { left: 58px; top: 150px; gap: 18px; }
  .card-front .brand-dot { width: 62px; height: 62px; }
  .card-front .brand-name { font-size: 25px; }

  .card-back .brand { left: 66px; top: 84px; gap: 12px; }
  .card-back .brand-dot { width: 36px; height: 36px; }
  .card-back .brand-name { font-size: 15px; }

  .backdrop-disc {
    position: absolute;
    left: 372px;
    top: 44px;
    width: 340px;
    height: 340px;
    border-radius: 50%;
    background: linear-gradient(180deg, var(--soft-top), var(--soft-bottom));
    opacity: 0.55;
  }

  .person {
    position: absolute;
    left: 361px;
    top: 89px;
    padding-left: 14px;
    border-left: 5px solid var(--brand-blue);
  }
  .person-name {
    font-family: "Saira", sans-serif;
    font-weight: 600;
    font-size: 31px;
    line-height: 1;
    color: var(--brand-blue);
  }
  .person-title {
    font-size: 17px;
    font-weight: 400;
    line-height: 1.1;
    color: var(--ink);
  }

  .contact-list {
    position: absolute;
    left: 64px;
    top: 238px;
    list-style: none;
  }
  .contact-item {
    display: flex;
    align-items: center;
    gap: 15px;
    height: 27px;
    font-size: 14.5px;
    font-weight: 600;
    letter-spacing: 0.02em;
  }
  .contact-icon { width: 17px; height: 17px; flex: none; }

  .address {
    position: absolute;
    left: 366px;
    top: 240px;
    font-style: normal;
    font-size: 14.5px;
    font-weight: 600;
    line-height: 20px;
    letter-spacing: 0.02em;
  }

  .footer-band {
    position: absolute;
    left: 0;
    right: 0;
    top: 341px;
    height: 21px;
    background: var(--brand-blue);
  }
</style>
</head>
<body>

<section class="card card-front">
  <div class="brand">
    <span class="brand-dot"></span>
    <span class="brand-name">MERIDIAN CARE CLINIC</span>
  </div>
  <div class="backdrop-disc"></div>
</section>

<section class="card card-back">
  <div class="brand">
    <span class="brand-dot"></span>
    <span class="brand-name">MERIDIAN CARE CLINIC</span>
  </div>

  <div class="person">
    <p class="person-name">YOUR NAME</p>
    <p class="person-title">Your Title</p>
  </div>

  <ul class="contact-list">
    <li class="contact-item">
      <svg class="contact-icon" viewBox="0 0 20 20" aria-hidden="true">
        <circle cx="10" cy="10" r="10" fill="var(--brand-blue)"/>
        <path d="M7 5.5c.6 0 1.4 1.6 1.4 2.1 0 .5-.8.8-.6 1.3.4 1 1.4 2 2.4 2.4.5.2.8-.6 1.3-.6.5 0 2.1.8 2.1 1.4 0 .8-1 1.6-1.8 1.6C9 13.7 6.3 11 6.3 7.3c0-.8.8-1.8.7-1.8z" fill="#fff"/>
      </svg>
      <span>012 345 6789</span>
    </li>
    <li class="contact-item">
      <svg class="contact-icon" viewBox="0 0 20 20" aria-hidden="true">
        <circle cx="10" cy="10" r="10" fill="var(--brand-blue)"/>
        <rect x="5.5" y="7" width="9" height="6.2" fill="none" stroke="#fff" stroke-width="1.2"/>
        <path d="M5.5 7l4.5 3.5L14.5 7" fill="none" stroke="#fff" stroke-width="1.2"/>
      </svg>
      <span>info@website.com</span>
    </li>
    <li class="contact-item">
      <svg class="contact-icon" viewBox="0 0 20 20" aria-hidden="true">
        <circle cx="10" cy="10" r="10" fill="var(--brand-blue)"/>
        <path d="M8 5.5v8.5l2-2 1.4 3 1.2-.6-1.4-2.9h2.8z" fill="#fff"/>
      </svg>
      <span>www.website.com</span>
    </li>
  </ul>

  <address class="address">
    Street name<br>
    Address for location<br>
    0000
  </address>

  <div class="footer-band"></div>
</section>

</body>
</html>
```